Optometrist Window poster "Retinal Photography Bulk Billed"

We are an optometry practice and we need a poster to highlight that we Bulk Bill retinal photography as part of the eye exam so there is no extra charge.

I've uploaded a Retinal Photograph which would need to be displayed in the poster.

The artwork will be displayed as a fabric banner in our shop window. We have 7 other banners with different services our business provides. The words needs to standout for passers by and the cars stopped at the traffic lights out front of our business. We already have signs with our logos phone number etc. so we won't need them included in the poster.

The size will be 1300mm width x 1900mm height

The Poster will need to say:
Have you had your photo taken?
Retinal Photography Bulk Billed

Target Market(s)

Passes by and cars stopped at traffic lights.

Industry/Entity Type

Optician

Requirements
Must have
• Have you had your photo taken?
• Retinal Photography Bulk Billed
• A Retinal Photograph

```html
<!DOCTYPE html>
<html lang="en">
<head>
<meta charset="utf-8">
<title>Retinal Photography Bulk Billed</title>
<link rel="stylesheet" href="https://fonts.googleapis.com/css2?family=Abril+Fatface&family=Poppins:wght@300;600&display=swap">
<style>
  :root {
    --paper: #ffffff;
    --wash: #e4e7e6;
    --wash-soft: #eef1f0;
    --ink: #3d4546;
    --muted: #5a6061;
    --retina-mid: #ec5a2c;
    --retina-deep: #d23a18;
  }
  html, body {
    margin: 0;
    padding: 0;
    width: 821px;
    height: 1200px;
    overflow: hidden;
    background: var(--paper);
  }
  .poster {
    position: relative;
    width: 821px;
    height: 1200px;
    overflow: hidden;
    background: var(--paper);
  }
  .brush-wash {
    position: absolute;
    inset: 0;
  }
  .retina-photo {
    position: absolute;
    left: 183px;
    top: 128px;
    width: 452px;
    height: 452px;
    border-radius: 50%;
    background: linear-gradient(135deg, var(--retina-mid), var(--retina-deep));
    box-shadow: 0 1px 3px rgba(0,0,0,0.15);
  }
  .headline {
    position: absolute;
    left: 0;
    right: 0;
    top: 648px;
    margin: 0;
    text-align: center;
    font-family: "Abril Fatface", "Playfair Display", serif;
    font-weight: 400;
    font-size: 68px;
    line-height: 80px;
    letter-spacing: 2px;
    color: var(--ink);
  }
  .headline span { display: block; }
  .divider {
    position: absolute;
    left: 384px;
    top: 1050px;
    width: 53px;
    height: 1px;
    background: var(--muted);
  }
  .service-line {
    position: absolute;
    left: 0;
    right: 0;
    top: 1122px;
    margin: 0;
    text-align: center;
    font-family: "Poppins", sans-serif;
    font-weight: 300;
    font-size: 18px;
    line-height: 28px;
    color: var(--muted);
  }
  .service-line strong { font-weight: 600; }
</style>
</head>
<body>
  <main class="poster">
    <svg class="brush-wash" width="821" height="1200" viewBox="0 0 821 1200" aria-hidden="true">
      <path d="M0 0 H821 V650 C660 630 480 640 320 600 C200 570 90 560 0 560 Z" fill="var(--wash)"/>
      <path d="M0 560 C160 590 360 640 560 660 C680 672 760 680 821 690 V860 C640 820 420 740 220 690 C120 665 50 650 0 645 Z" fill="var(--wash-soft)"/>
    </svg>

    <div class="retina-photo" role="img" aria-label="Retinal photograph of the back of the eye"></div>

    <h1 class="headline">
      <span>HAVE YOU</span>
      <span>HAD</span>
      <span>YOUR PHOTO</span>
      <span>TAKEN?</span>
    </h1>

    <div class="divider"></div>

    <p class="service-line">Retinal Photography <strong>Bulk Billed</strong></p>
  </main>
</body>
</html>
```